Postcard design to acquire new clients for my Property Management Company

I'm looking for a postcard design that I can send to prospective clients detailing information about my company and services.
Postcard should be eye catching and contain information from www.brightkeyrentals-example.com. I've provided a few screen shots for the most important information and my logo.
Target Market(s)
Real Estate
Industry/Entity Type
Real Estate
Font styles to use
Sans Serif
Requirements
Must have
- Must be eye catching!! this will be a direct mail piece - I'd like for the card to be read and not tossed in the trash immediately.
Design que from the logo.
A place to write / print the receipts name and address.
our physical address - 2287 Marble Lane, Lubbock, TX 79555.
Should not have
- the contact information on the business card is not accurate - please use info from website.

```html
<!DOCTYPE html>
<html lang="en">
<head>
<meta charset="utf-8">
<title>BrightKey Property Management – Direct Mail Postcard</title>
<link href="https://fonts.googleapis.com/css2?family=Montserrat:ital,wght@0,400;0,500;0,600;0,700;0,800;1,500;1,600&display=swap" rel="stylesheet">
<style>
  :root{
    --navy:#1b3f86;
    --blue:#2456ad;
    --blue-dark:#173a80;
    --blue-pale:#c8d8f1;
    --gray:#9a9ea4;
    --gray-light:#d3d6da;
    --text:#3a3f47;
    --white:#ffffff;
    --stage:#8c8f93;
  }
  *{margin:0;padding:0;box-sizing:border-box}
  html,body{width:1200px;height:1200px;overflow:hidden;background:var(--stage);font-family:"Montserrat",sans-serif}
  .postcard{position:absolute;left:127px;width:867px;height:472px;background:var(--white);transform:scale(1.09);transform-origin:top left;overflow:hidden;box-shadow:0 6px 14px rgba(0,0,0,.35)}
  .postcard--front{top:48px}
  .postcard--back{top:618px}
  .shapes{position:absolute;inset:0;width:867px;height:472px}
  .abs{position:absolute}

  /* brand */
  .brand{color:var(--navy);font-weight:600;text-transform:uppercase;line-height:1}
  .brand__name{font-size:31px;letter-spacing:5px}
  .brand__sub{font-size:14.5px;letter-spacing:3.6px;margin-top:6px}

  /* front */
  .headline{left:26px;top:86px;color:var(--white);text-transform:uppercase;line-height:1.05}
  .headline__main{font-size:26px;font-weight:600;letter-spacing:.3px}
  .headline__sub{font-size:19.5px;font-weight:500;letter-spacing:.6px;margin-top:2px}
  .offer{left:25px;top:159px;font-size:15px;font-weight:500;color:var(--blue)}
  .region{left:625px;top:79px;width:235px;text-align:center;color:var(--white);font-size:14px;font-weight:600;line-height:1.1}
  .service{position:absolute;width:238px;display:flex;gap:10px}
  .service--right{width:228px}
  .service__icon{width:56px;height:46px;flex:none}
  .service__title{font-size:12.5px;font-weight:700;color:var(--blue);text-transform:uppercase;line-height:1.1;white-space:nowrap}
  .service__text{font-size:9.3px;color:var(--text);line-height:1.15;margin-top:1px}
  .web{display:flex;align-items:center;gap:6px;font-size:11.5px;font-weight:600;color:var(--blue-dark);white-space:nowrap}
  .web svg{flex:none}

  /* back */
  .contact-label{left:12px;top:13px;color:var(--white);font-size:14px;font-weight:700;letter-spacing:.3px}
  .contact-line{left:205px;top:11px;display:flex;align-items:center;gap:4px;font-size:15px;font-weight:700;color:var(--navy);white-space:nowrap}
  .contact-line svg{flex:none}
  .praise{left:72px;top:59px;width:500px;color:var(--white)}
  .praise__title{font-size:16.5px;font-weight:700;text-transform:uppercase}
  .praise__quote{font-size:9.6px;font-style:italic;font-weight:500;line-height:1.3;margin-top:2px}
  .praise__quote b{font-weight:700}
  .plan{position:absolute;background:var(--white);border-radius:8px;overflow:hidden;box-shadow:0 2px 6px rgba(0,0,0,.25)}
  .plan__head{background:var(--gray);color:var(--white);text-align:center;padding:4px 0 3px;text-transform:uppercase;font-weight:700;font-size:13.5px;line-height:1.05}
  .plan__tag{font-size:10px;font-weight:500;text-transform:none;letter-spacing:.2px}
  .plan--featured .plan__head{background:var(--blue-dark);font-size:15px;padding-top:6px}
  .plan__price{margin:8px auto 10px;width:126px;border:1.5px solid var(--blue);text-align:center;color:var(--blue);line-height:1}
  .plan__rate{font-size:16px;font-weight:700;padding-top:3px}
  .plan__unit{font-size:10.5px;font-weight:500;padding:2px 0 4px}
  .plan__list{list-style:none;padding:0 6px 0 8px;font-size:10.5px;font-weight:500;color:var(--navy);line-height:1.25}
  .plan__list li{padding-left:9px;position:relative}
  .plan__list li::before{content:"✓";position:absolute;left:-1px;color:var(--blue);font-size:9px}
  .plan__list strong{font-weight:700}
  .stars{left:208px;top:142px;color:var(--navy);font-size:10px;letter-spacing:1.5px}
</style>
</head>
<body>

<!-- FRONT -->
<section class="postcard postcard--front">
  <svg class="shapes" viewBox="0 0 867 472">
    <defs>
      <linearGradient id="bannerFront" x1="0" x2="1"><stop offset="0" stop-color="#2a5cb3"/><stop offset="1" stop-color="#173a80"/></linearGradient>
      <linearGradient id="photoTone" x1="0" y1="0" x2="1" y2="1"><stop offset="0" stop-color="#eef2f7"/><stop offset=".45" stop-color="#c9d3e0"/><stop offset=".75" stop-color="#e7b79d"/><stop offset="1" stop-color="#9aa6b6"/></linearGradient>
    </defs>
    <polygon points="0,0 92,0 62,70 0,70" fill="#c7cace"/>
    <polygon points="100,0 114,0 84,70 70,70" fill="#b3b7bc"/>
    <polygon points="0,72 635,72 598,150 0,150" fill="url(#bannerFront)"/>
    <rect x="3" y="82" width="5" height="62" fill="#fff"/>
    <polygon points="0,152 598,152 584,183 0,183" fill="var(--blue-pale)"/>
    <polygon points="650,23 867,23 867,118 612,118" fill="url(#bannerFront)"/>
    <polygon points="612,118 867,118 867,128 607,128" fill="#12306b"/>
    <polygon points="603,150 618,150 481,460 466,460" fill="var(--gray-light)"/>
    <polygon points="640,128 867,128 867,460 505,460" fill="url(#photoTone)" role="img" aria-label="Photo of a small model house beside a laptop on a desk"/>
    <circle cx="747" cy="38" r="28" fill="#fff" stroke="#b7bbc0" stroke-width="3"/>
    <rect x="0" y="460" width="867" height="12" fill="var(--blue-dark)"/>
    <polygon points="598,432 867,432 867,460 585,460" fill="#fff"/>
  </svg>

  <div class="abs brand" style="left:130px;top:12px">
    <div class="brand__name">BrightKey</div>
    <div class="brand__sub">Property Management</div>
  </div>

  <h1 class="abs headline">
    <div class="headline__main">Maximize your financial returns</div>
    <div class="headline__sub">With support from our rental specialists</div>
  </h1>
  <p class="abs offer">We offer FULL-SERVICE property management solutions</p>
  <p class="abs region">PROPERTY MANAGEMENT<br>ACROSS LUBBOCK, TX</p>

  <div class="service" style="left:15px;top:210px">
    <svg class="service__icon" viewBox="0 0 56 46"><polygon points="28,0 56,46 0,46" fill="var(--gray)"/><path d="M18 38V28l10-8 10 8v10h-7v-6h-6v6z" fill="#fff"/></svg>
    <div><h3 class="service__title">Property Marketing</h3><p class="service__text">Let us take over your marketing for you and we'll find a qualified renter quickly.</p></div>
  </div>
  <div class="service" style="left:15px;top:272px">
    <svg class="service__icon" viewBox="0 0 56 46"><polygon points="28,0 56,46 0,46" fill="var(--gray)"/><circle cx="28" cy="24" r="4" fill="#fff"/><circle cx="20" cy="28" r="3.3" fill="#fff"/><circle cx="36" cy="28" r="3.3" fill="#fff"/><path d="M14 40q6-9 12 0zM30 40q6-9 12 0zM21 40q7-11 14 0z" fill="#fff"/></svg>
    <div><h3 class="service__title">Tenant Screening</h3><p class="service__text">We screen all applications using fair housing guidelines to protect you.</p></div>
  </div>
  <div class="service" style="left:15px;top:332px">
    <svg class="service__icon" viewBox="0 0 56 46"><polygon points="28,0 56,46 0,46" fill="var(--gray)"/><circle cx="30" cy="24" r="6" fill="none" stroke="#fff" stroke-width="2"/><text x="30" y="27.5" font-size="9" font-weight="700" fill="#fff" text-anchor="middle" font-family="Montserrat,sans-serif">$</text><path d="M14 38h10l8-3h6" fill="none" stroke="#fff" stroke-width="2.5"/></svg>
    <div><h3 class="service__title">Rent Collection</h3><p class="service__text">Stop guessing when you'll receive your rental earnings every month &amp; say hello to consistent payments.</p></div>
  </div>
  <div class="service" style="left:15px;top:392px">
    <svg class="service__icon" viewBox="0 0 56 46"><polygon points="28,0 56,46 0,46" fill="var(--gray)"/><circle cx="26" cy="28" r="6" fill="none" stroke="#fff" stroke-width="2.5"/><path d="M30 32l7 7" stroke="#fff" stroke-width="3"/></svg>
    <div><h3 class="service__title">Property Inspections</h3><p class="service__text">Inspections form an important part of our proactive property management approach.</p></div>
  </div>

  <div class="service service--right" style="left:262px;top:210px">
    <svg class="service__icon" viewBox="0 0 56 46"><polygon points="28,0 56,46 0,46" fill="var(--gray)"/><path d="M28 17v21M18 22h20M22 40h12" stroke="#fff" stroke-width="2"/><path d="M15 30l3-8 3 8zM35 30l3-8 3 8z" fill="#fff"/></svg>
    <div><h3 class="service__title">Legal Guidance</h3><p class="service__text">Don't accidentally violate one of the many ordinances &amp; housing laws governing your relationship with your tenants.</p></div>
  </div>
  <div class="service service--right" style="left:262px;top:272px">
    <svg class="service__icon" viewBox="0 0 56 46"><polygon points="28,0 56,46 0,46" fill="var(--gray)"/><rect x="19" y="32" width="4" height="7" fill="#fff"/><rect x="25" y="28" width="4" height="11" fill="#fff"/><rect x="31" y="24" width="4" height="15" fill="#fff"/><path d="M17 28l8-6 5 3 8-7" fill="none" stroke="#fff" stroke-width="1.8"/></svg>
    <div><h3 class="service__title">Financial Reporting</h3><p class="service__text">We generate monthly statements so you can review income &amp; expenses at a moment's notice.</p></div>
  </div>
  <div class="service service--right" style="left:262px;top:332px">
    <svg class="service__icon" viewBox="0 0 56 46"><polygon points="28,0 56,46 0,46" fill="var(--gray)"/><path d="M28 18l9 3v7c0 6-4 9-9 11-5-2-9-5-9-11v-7z" fill="none" stroke="#fff" stroke-width="2"/><path d="M24 28l3 3 5-6" fill="none" stroke="#fff" stroke-width="2"/></svg>
    <div><h3 class="service__title">Evictions</h3><p class="service__text">We will handle evictions for you &amp; find new renters when its over.</p></div>
  </div>
  <div class="service service--right" style="left:262px;top:392px">
    <svg class="service__icon" viewBox="0 0 56 46"><polygon points="28,0 56,46 0,46" fill="var(--gray)"/><path d="M19 22l16 16M37 22L21 38" stroke="#fff" stroke-width="3" stroke-linecap="round"/></svg>
    <div><h3 class="service__title">Maintenance</h3><p class="service__text">Let us coordinate repair work on your behalf!</p></div>
  </div>

  <div class="abs web" style="left:600px;top:439px">
    <svg width="15" height="15" viewBox="0 0 16 16"><circle cx="8" cy="8" r="7" fill="none" stroke="currentColor" stroke-width="1.6"/><ellipse cx="8" cy="8" rx="3" ry="7" fill="none" stroke="currentColor" stroke-width="1.3"/><path d="M1 8h14" stroke="currentColor" stroke-width="1.3"/></svg>
    www.brightkeyrentals-example.com
  </div>
</section>

<!-- BACK -->
<section class="postcard postcard--back">
  <svg class="shapes" viewBox="0 0 867 472">
    <defs>
      <linearGradient id="bannerBack" x1="0" x2="1"><stop offset="0" stop-color="#2a5cb3"/><stop offset="1" stop-color="#173a80"/></linearGradient>
      <linearGradient id="pricingGlow" x1="0" y1="0" x2="0" y2="1"><stop offset="0" stop-color="#ffffff"/><stop offset=".45" stop-color="#dfe7f3"/><stop offset="1" stop-color="#2456ad"/></linearGradient>
    </defs>
    <rect x="0" y="0" width="867" height="42" fill="#fff"/>
    <polygon points="0,0 205,0 186,42 0,42" fill="var(--gray)"/>
    <polygon points="0,45 630,45 582,131 0,131" fill="url(#bannerBack)"/>
    <polygon points="630,45 642,45 594,131 582,131" fill="#173a80"/>
    <polygon points="0,131 582,131 462,463 0,463" fill="url(#pricingGlow)"/>
    <polygon points="600,131 612,131 492,463 480,463" fill="#eef0f3"/>
    <polygon points="612,0 867,0 867,92 600,92" fill="#fff"/>
    <polygon points="592,432 867,432 867,463 579,463" fill="var(--blue-dark)"/>
    <polygon points="570,432 582,432 569,463 557,463" fill="var(--gray-light)"/>
    <rect x="0" y="463" width="867" height="9" fill="var(--gray)"/>
  </svg>

  <p class="abs contact-label">CONTACT OUR TEAM</p>
  <div class="abs contact-line">
    <svg width="17" height="17" viewBox="0 0 17 17"><circle cx="8.5" cy="8.5" r="8" fill="var(--navy)"/><path d="M5.5 4.5l2 2-1 1.2c.7 1.4 1.6 2.3 3 3l1.2-1 2 2-1.2 1.3c-3.4-.4-6-3-6.4-6.4z" fill="#fff"/></svg>
    (806) 555-0142
    <svg width="17" height="17" viewBox="0 0 17 17" style="margin-left:4px"><circle cx="8.5" cy="8.5" r="8" fill="var(--navy)"/><rect x="4" y="5.5" width="9" height="6" fill="none" stroke="#fff" stroke-width="1.2"/><path d="M4 5.5l4.5 3.5 4.5-3.5" fill="none" stroke="#fff" stroke-width="1.2"/></svg>
    <span style="font-size:12.5px">info@brightkeyrentals-example.com</span>
    <svg width="16" height="16" viewBox="0 0 16 16" style="margin-left:3px"><circle cx="8" cy="8" r="7.5" fill="var(--navy)"/></svg>
  </div>

  <div class="abs brand" style="left:626px;top:30px">
    <div class="brand__name" style="font-size:26px;letter-spacing:4.5px">BrightKey</div>
    <div class="brand__sub" style="font-size:12px;letter-spacing:3px;margin-top:4px">Property Management</div>
  </div>

  <svg class="abs" style="left:12px;top:60px" width="50" height="60" viewBox="0 0 50 60">
    <path d="M10 7l3 5M22 2v6M33 7l-3 5" stroke="#fff" stroke-width="2.5" stroke-linecap="round"/>
    <rect x="3" y="28" width="9" height="26" fill="none" stroke="#fff" stroke-width="3"/>
    <path d="M15 30l8-12c2-3 6-2 6 2l-2 8h11c3 0 5 3 4 5l-4 17c-1 2-2 3-4 3H15z" fill="none" stroke="#fff" stroke-width="3" stroke-linejoin="round"/>
  </svg>
  <div class="abs praise">
    <h2 class="praise__title">Your satisfaction is our priority</h2>
    <p class="praise__quote">"Dana has been very understanding and willing to work with us on anything that has came up. We moved here from San Antonio, and they were there when we needed our keys on the weekend. Any questions I've had, Dana has been there to help me with it." <b>-Laura P.</b></p>
  </div>

  <div class="abs stars">★★★★★</div>

  <article class="plan" style="left:17px;top:170px;width:143px;height:261px">
    <header class="plan__head">Lease Only<div class="plan__tag">- You Just Need Tenants -</div></header>
    <div class="plan__price"><div class="plan__rate">9%</div><div class="plan__unit">of Annual Lease</div></div>
    <ul class="plan__list">
      <li>Professional Photography</li>
      <li>Marketing &amp; Advertising</li>
      <li>Property Showings</li>
      <li>Tenant Screening &amp; Qualifications</li>
      <li>Lease Execution</li>
      <li>Move In Coordination</li>
    </ul>
  </article>

  <article class="plan plan--featured" style="left:163px;top:156px;width:148px;height:289px;z-index:2">
    <header class="plan__head">Full Service<div class="plan__tag">- Our Most Popular -</div></header>
    <div class="plan__price"><div class="plan__rate">10%</div><div class="plan__unit">of Annual Lease</div></div>
    <ul class="plan__list">
      <li><strong>Includes Leasing Service +</strong></li>
      <li>24/7 Emergency Response</li>
      <li>Move In &amp; Out Inspections</li>
      <li>Professional Lease Enforcement</li>
      <li>Schedule &amp; Oversee all Repairs</li>
      <li>Pay all Invoices</li>
      <li>Monthly &amp; Year End Statements</li>
      <li>Annual Market Rent Analysis</li>
    </ul>
  </article>

  <article class="plan" style="left:312px;top:170px;width:146px;height:261px">
    <header class="plan__head">Premium Service<div class="plan__tag">- Our Premier Service -</div></header>
    <div class="plan__price"><div class="plan__rate">12%</div><div class="plan__unit">of Annual Lease</div></div>
    <ul class="plan__list">
      <li><strong>Includes Full Service Features +</strong></li>
      <li>Professional Video Marketing</li>
      <li>Home Warranty Coordination</li>
      <li>Tenant Retention Program</li>
    </ul>
  </article>

  <div class="abs web" style="left:600px;top:440px;color:#fff">
    <svg width="15" height="15" viewBox="0 0 16 16"><circle cx="8" cy="8" r="7" fill="none" stroke="currentColor" stroke-width="1.6"/><ellipse cx="8" cy="8" rx="3" ry="7" fill="none" stroke="currentColor" stroke-width="1.3"/><path d="M1 8h14" stroke="currentColor" stroke-width="1.3"/></svg>
    www.brightkeyrentals-example.com
  </div>
</section>

</body>
</html>
```